Need new look for home page of Makeup Artist Site

We want a new, clean, modern, professional look for the new design for our website. Our current site is at https://glowvra.com. We would like a high fashion site with diverse ethnic groups represented throughout the page. We like trelk.com as an example of style and user experience. This website is for people to look for a makeup artist or esthetician to come to their home and perform a service there. They will pay on the website and be able to review available service providers and choose one. We will need 2 additional pages once this design is approved. We will pay separately for those.

```html
<!DOCTYPE html>
<html lang="en">
<head>
<meta charset="utf-8">
<title>Glowvra – Beauty &amp; Facial Care at Home</title>
<link href="https://fonts.googleapis.com/css2?family=Tinos:wght@400;700&display=swap" rel="stylesheet">
<style>
:root{
  --red:#e0282a;
  --ink:#1a1a1a;
  --dark:#141414;
  --footer:#111111;
  --hero-bg:#e3e8e2;
  --muted:#333333;
  --line:#d9d9d9;
  --white:#ffffff;
}
*{margin:0;padding:0;box-sizing:border-box}
html,body{width:1200px;height:3660px;overflow:hidden}
body{position:relative;font-family:"Tinos","Times New Roman",serif;color:var(--ink);background:var(--white)}
.abs{position:absolute}
a{color:inherit;text-decoration:none}
.btn{position:absolute;display:flex;align-items:center;justify-content:center;background:var(--red);color:var(--white);border-radius:22px;font-size:12px;white-space:nowrap}
.ph{position:absolute}

/* header */
.brand{position:absolute;left:155px;top:30px;font-size:26px;font-weight:700;color:var(--red);letter-spacing:1px}
.nav a{position:absolute;top:38px;font-size:10.5px;color:var(--ink);white-space:nowrap}
.portal{left:831px;top:30px;width:97px;height:30px;font-size:10.5px}
.tools{position:absolute;left:950px;top:34px;display:flex;gap:16px}
.cart-badge{position:absolute;left:1027px;top:45px;width:14px;height:14px;border-radius:50%;background:var(--red);color:#fff;font-size:9px;display:flex;align-items:center;justify-content:center}

/* hero */
.hero{left:0;top:0;width:1200px;height:670px;background:var(--hero-bg)}
.hero-photo{left:590px;top:60px;width:480px;height:610px;background:radial-gradient(ellipse at 55% 45%,#d8b49c 0%,#8a5a44 45%,rgba(227,232,226,0) 75%)}
.hero-line{position:absolute;left:156px;font-size:38px;color:var(--ink)}
.hero-accent{position:absolute;left:156px;top:272px;font-size:47px;font-weight:700;color:var(--red)}
.hero-cta{left:159px;top:415px;width:98px;height:30px;font-size:11px}

/* clients */
.clients{left:0;top:670px;width:1200px;height:602px;background:var(--dark)}
.clients-photo{left:660px;top:670px;width:540px;height:602px;background:radial-gradient(circle at 65% 30%,#a0603c 0%,#5a3322 25%,transparent 45%),radial-gradient(circle at 35% 55%,#c9a27a 0%,#8d6a4a 22%,transparent 30%),radial-gradient(circle at 60% 92%,#f1cfb8 0%,#e3b596 28%,transparent 38%),linear-gradient(90deg,var(--dark) 0%,#2a2220 60%,#3a2a22 100%)}
.kicker{position:absolute;font-size:15px;letter-spacing:3px}
.section-title{position:absolute;font-size:55px;font-weight:400;white-space:nowrap}
.step{position:absolute;width:180px;text-align:center;color:#fff}
.step svg{display:block;margin:0 auto 14px}
.step h3{font-size:19px;font-weight:700;margin-bottom:12px;white-space:nowrap}
.step p{font-size:11px;line-height:22px}
.rule{position:absolute;height:1px;background:#fff}

/* consultants */
.cons-photo{left:482px;top:1310px;width:268px;height:495px;background:linear-gradient(180deg,#e8cf9a 0%,#d9b27a 35%,#f0f0ec 55%,#1fb7a3 80%,#17a893 100%);border-radius:134px 134px 0 0}
.perk{position:absolute;left:148px;width:320px;z-index:2}
.perk .dot{position:absolute;left:0;top:0;width:70px;height:70px;border-radius:50%;background:var(--red);display:flex;align-items:center;justify-content:center}
.perk h3{position:absolute;left:88px;font-size:17px;font-weight:700;white-space:nowrap}
.perk p{position:absolute;left:88px;width:210px;font-size:11px;line-height:24px;color:var(--muted)}
.divider{position:absolute;left:152px;width:302px;height:1px;background:var(--line)}

/* why */
.why-photo{left:0;top:1805px;width:1200px;height:545px;background:linear-gradient(90deg,#7a5440 0%,#e9dcd2 18%,#f2ebe5 40%,#e9ddd3 70%,#d8c4b5 100%)}
.why-title{left:604px;top:1870px;font-size:52px}
.why-box{left:600px;top:1958px;width:445px;height:345px;background:#fff;padding:22px 24px 0 26px}
.why-box li{list-style:none;position:relative;padding-left:28px;font-size:11px;line-height:38px;color:var(--muted)}
.why-box li::before{content:"";position:absolute;left:2px;top:15px;width:10px;height:8px;background:var(--red);clip-path:polygon(0 50%,100% 0,70% 50%,100% 100%)}

/* services */
.services-photo{left:820px;top:2380px;width:380px;height:800px;background:radial-gradient(ellipse at 55% 40%,#e7e7e7 0%,#f3f3f3 40%,rgba(255,255,255,0) 70%)}
.services-title{left:0;top:2408px;width:1200px;text-align:center;font-size:30px}
.service{position:absolute;width:260px}
.service h3{font-size:23px;font-weight:400;margin:20px 0 12px;white-space:nowrap}
.service p{font-size:11px;line-height:29px;color:var(--muted)}
.service a{display:inline-block;margin-top:10px;font-size:11px;color:var(--red);text-decoration:underline}

/* cta + footer */
.footer{left:0;top:3268px;width:1200px;height:392px;background:var(--footer)}
.cta{left:142px;top:3185px;width:916px;height:122px;background:var(--red)}
.cta-text{left:215px;top:3225px;font-size:30px;color:#fff;white-space:nowrap}
.cta-btn{left:851px;top:3226px;width:137px;height:40px;background:#fff;color:var(--red);font-size:14px;border-radius:22px}
.foot-brand{left:150px;top:3383px;width:257px;height:87px;background:#fff;border-radius:16px;display:flex;align-items:center;justify-content:center;font-size:40px;font-weight:700;color:var(--red);letter-spacing:2px}
.social{position:absolute;top:3512px;width:30px;height:30px;background:#3b5c9a}
.foot-title{position:absolute;top:3378px;font-size:23px;color:#fff}
.foot-title::after{content:"";position:absolute;left:0;top:36px;width:64px;height:3px;background:var(--red)}
.foot-links{position:absolute;top:3450px;font-size:11px;line-height:27px;color:#fff;list-style:none}
.contact{position:absolute;left:842px;font-size:11px;color:#fff;display:flex;align-items:center;gap:14px}
.foot-rule{left:142px;top:3606px;width:916px;height:1px;background:#555}
.copy{left:0;top:3628px;width:1200px;text-align:center;font-size:11px;color:#fff}
</style>
</head>
<body>

<!-- hero -->
<section class="abs hero"></section>
<div class="ph hero-photo" role="img" aria-label="Portrait of a woman with curly brown hair and red nails"></div>
<div class="brand">GLOWVRA</div>
<nav class="nav">
  <a style="left:354px">Home</a>
  <a style="left:406px">Our Services</a>
  <a style="left:486px">Consultants</a>
  <a style="left:561px">Apply to Be a Consultant</a>
  <a style="left:693px">Glowvra Street</a>
  <a style="left:778px">Location</a>
</nav>
<a class="btn portal">Consultant Portal</a>
<div class="tools">
  <svg width="16" height="16" viewBox="0 0 16 16" fill="none" stroke="#333" stroke-width="1.3"><circle cx="8" cy="5" r="3.2"/><path d="M2 15c0-3.5 2.7-5.5 6-5.5s6 2 6 5.5z"/></svg>
  <svg width="16" height="16" viewBox="0 0 16 16" fill="none" stroke="#333" stroke-width="1.5"><circle cx="7" cy="7" r="5"/><path d="M11 11l4 4"/></svg>
  <svg width="16" height="16" viewBox="0 0 16 16" fill="none" stroke="#333" stroke-width="1.3"><path d="M2 5h12l-1 10H3z"/><path d="M5 5V4a3 3 0 016 0v1"/></svg>
</div>
<div class="cart-badge">0</div>
<div class="hero-line" style="top:226px">We Provide</div>
<div class="hero-accent">Beauty &amp; Facial care</div>
<div class="hero-line" style="top:334px">services in your home.</div>
<a class="btn hero-cta">Learn More</a>

<!-- for clients -->
<section class="abs clients"></section>
<div class="ph clients-photo" role="img" aria-label="Makeup powders, bronzing pearls and a brush on a dark surface"></div>
<div class="kicker" style="left:155px;top:755px;color:#fff">How Glowvra Works</div>
<div class="section-title" style="left:155px;top:772px;color:#fff">For Clients</div>

<div class="step" style="left:126px;top:902px">
  <svg width="14" height="36" viewBox="0 0 14 36" fill="#fff"><rect x="4" y="0" width="6" height="10" rx="2"/><rect x="2" y="12" width="10" height="6"/><rect x="1" y="19" width="12" height="17"/></svg>
  <h3>Explore</h3>
  <p>First, choose from our<br>makeup or facial care<br>services.</p>
</div>
<div class="step" style="left:287px;top:902px">
  <svg width="32" height="36" viewBox="0 0 32 36" fill="none" stroke="#fff" stroke-width="3"><rect x="2" y="6" width="28" height="28" rx="2"/><path d="M9 1v8M23 1v8M2 13h28"/><g fill="#fff" stroke="none"><rect x="8" y="18" width="4" height="4"/><rect x="14" y="18" width="4" height="4"/><rect x="20" y="18" width="4" height="4"/><rect x="8" y="25" width="4" height="4"/><rect x="14" y="25" width="4" height="4"/><rect x="20" y="25" width="4" height="4"/></g></svg>
  <h3>Schedule</h3>
  <p>Once you have made your<br>selection, choose from our<br>listing of vetted consultants</p>
</div>
<div class="step" style="left:462px;top:902px">
  <svg width="38" height="36" viewBox="0 0 38 36" fill="#fff"><path d="M19 2L1 18l3 3 3-2.7V34h10V25h4v9h10V18.3l3 2.7 3-3z"/></svg>
  <h3>Pay &amp; Get Glowvra</h3>
  <p>Our Consultant will come<br>to you at the scheduled<br>time in the comfort of your</p>
</div>
<div class="rule" style="left:117px;top:1124px;width:38px"></div>
<a class="btn" style="left:165px;top:1104px;width:160px;height:39px;font-size:11px">Explore Makeup Looks</a>

<!-- for consultants -->
<div class="ph cons-photo" role="img" aria-label="Blonde makeup artist holding brushes, wearing a white vest over a teal top"></div>
<div class="kicker" style="left:695px;top:1323px;color:var(--ink)">How Glowvra Works</div>
<div class="section-title" style="left:695px;top:1340px">For Consultants</div>
<div class="rule" style="left:726px;top:1459px;width:37px;background:#333"></div>
<a class="btn" style="left:773px;top:1440px;width:142px;height:39px;font-size:11px">Join Glowvra Network</a>

<div class="perk" style="top:1397px">
  <div class="dot"><svg width="38" height="30" viewBox="0 0 38 30" fill="#fff"><circle cx="19" cy="8" r="5"/><circle cx="8" cy="11" r="4"/><circle cx="30" cy="11" r="4"/><path d="M11 28c0-6 4-10 8-10s8 4 8 10z"/><path d="M1 27c0-5 3-8 7-8 2 0 3 1 4 2-1 2-2 4-2 6z"/><path d="M37 27c0-5-3-8-7-8-2 0-3 1-4 2 1 2 2 4 2 6z"/></svg></div>
  <h3 style="top:-10px">Build Your Client Base</h3>
  <p style="top:18px">Don't pay for expensive marketing. Let us find clients for you.</p>
</div>
<div class="divider" style="top:1497px"></div>
<div class="perk" style="top:1537px">
  <div class="dot"><svg width="36" height="36" viewBox="0 0 36 36" fill="none" stroke="#fff" stroke-width="3"><circle cx="18" cy="18" r="15"/><path d="M18 9v10h7"/></svg></div>
  <h3 style="top:-6px">Manage Your Business</h3>
  <p style="top:22px">You're always in control of your hours and your appointments.</p>
</div>
<div class="divider" style="top:1647px"></div>
<div class="perk" style="top:1677px">
  <div class="dot"><svg width="36" height="26" viewBox="0 0 36 26" fill="#fff"><path d="M7 2h22l4 9h2v10h-3v4h-5v-4H9v4H4v-4H1V11h2z"/><g fill="var(--red)"><path d="M9 5h18l2.5 6h-23z"/><circle cx="8" cy="16" r="2.5"/><circle cx="28" cy="16" r="2.5"/></g></svg></div>
  <h3 style="top:-5px">Check Appointments and Go!</h3>
  <p style="top:23px">Just log in and check your appointments the day before and you're set.</p>
</div>

<!-- why -->
<div class="ph why-photo" role="img" aria-label="Woman relaxing with a white facial mask, brushes at the side"></div>
<div class="abs why-title">Why Glowvra?</div>
<ul class="abs why-box">
  <li>Access to service of the Washington Metropolitan area's most qualified and vetted professional makeup artists and estheticians</li>
  <li>Convenience of having your makeup done in your home or at a location of your choosing</li>
  <li>Sessions booked according to your schedule</li>
  <li>Select the look that you want for any occasion</li>
  <li>Preliminary test run included for your most important events</li>
  <li>Access to Glowvra Street's blogs, tips, trends and makeup events</li>
</ul>

<!-- services -->
<div class="ph services-photo" role="img" aria-label="Faint monochrome portrait of a woman touching her cheek"></div>
<h2 class="abs services-title" style="font-weight:400">Our Services</h2>

<div class="service" style="left:160px;top:2548px">
  <svg width="34" height="44" viewBox="0 0 34 44" fill="none" stroke="var(--red)" stroke-width="1.6"><circle cx="17" cy="26" r="13"/><path d="M11 6l6-5 6 5-6 7z"/></svg>
  <h3>Weddings</h3>
  <p>Cras sit amet sapien non dolor posuere scelerisque. Interdum et malesuada fames ac ante ipsum primis in faucibus. Ut eget elementum ligula.</p>
  <a>Learn More</a>
</div>
<div class="service" style="left:474px;top:2548px">
  <svg width="34" height="44" viewBox="0 0 34 44" fill="none" stroke="var(--red)" stroke-width="1.6"><path d="M8 42l10-22 6 3-10 22z"/><path d="M18 20c2-8 8-16 14-18-1 7-5 15-8 21z"/></svg>
  <h3>Full Makeup Application</h3>
  <p>Cras sit amet sapien non dolor posuere scelerisque. Interdum et malesuada fames ac ante ipsum primis in faucibus. Ut eget elementum ligula.</p>
  <a>Learn More</a>
</div>
<div class="service" style="left:789px;top:2548px">
  <svg width="46" height="44" viewBox="0 0 46 44" fill="none" stroke="var(--red)" stroke-width="1.6"><rect x="3" y="14" width="40" height="8"/><rect x="6" y="22" width="34" height="20"/><path d="M23 14v28M23 14c-4-10-14-10-12-2 1 3 8 2 12 2zM23 14c4-10 14-10 12-2-1 3-8 2-12 2z"/></svg>
  <h3>Gift Certificates</h3>
  <p>Cras sit amet sapien non dolor posuere scelerisque. Interdum et malesuada fames ac ante ipsum primis in faucibus. Ut eget elementum ligula.</p>
  <a>Learn More</a>
</div>

<div class="service" style="left:160px;top:2844px">
  <svg width="44" height="44" viewBox="0 0 44 44" fill="none" stroke="var(--red)" stroke-width="1.6"><rect x="12" y="28" width="12" height="15"/><rect x="13" y="19" width="10" height="9"/><path d="M14 19V9l8-5v15"/><path d="M34 20l2 3 3 .5-2 2 .5 3-3-1.5-3 1.5.5-3-2-2 3-.5z"/><path d="M6 6l1.5 2.5 2.5.5-2 1.5.5 2.5-2.5-1-2.5 1 .5-2.5-2-1.5 2.5-.5z"/></svg>
  <h3>Group Party</h3>
  <p>Cras sit amet sapien non dolor posuere scelerisque. Interdum et malesuada fames ac ante ipsum primis in faucibus. Ut eget elementum ligula.</p>
  <a>Learn More</a>
</div>
<div class="service" style="left:474px;top:2844px">
  <svg width="44" height="44" viewBox="0 0 44 44" fill="none" stroke="var(--red)" stroke-width="1.6"><path d="M22 4c8 10 14 17 14 25a14 14 0 01-28 0c0-8 6-15 14-25z"/><path d="M16 30a6 6 0 006 6"/></svg>
  <h3>Facial Care Services</h3>
  <p>Cras sit amet sapien non dolor posuere scelerisque. Interdum et malesuada fames ac ante ipsum primis in faucibus. Ut eget elementum ligula.</p>
  <a>Learn More</a>
</div>
<div class="service" style="left:789px;top:2844px">
  <svg width="44" height="44" viewBox="0 0 44 44" fill="none" stroke="var(--red)" stroke-width="1.6"><rect x="3" y="8" width="38" height="28" rx="3"/><path d="M18 15v14l11-7z"/><path d="M14 42h16"/></svg>
  <h3>Beauty Tutorials</h3>
  <p>Cras sit amet sapien non dolor posuere scelerisque. Interdum et malesuada fames ac ante ipsum primis in faucibus. Ut eget elementum ligula.</p>
  <a>Learn More</a>
</div>

<!-- cta + footer -->
<footer class="abs footer"></footer>
<div class="abs cta"></div>
<div class="abs cta-text">Go ahead and revel in your Glowvra experience!</div>
<a class="btn cta-btn">Get Started!</a>

<div class="abs foot-brand">GLOWVRA</div>
<div class="social" style="left:155px"></div>
<div class="social" style="left:202px"></div>

<div class="foot-title" style="left:510px">Quick Links</div>
<ul class="foot-links" style="left:522px"><li>About Us</li><li>Support</li><li>FAQs</li><li>Lost &amp; Found</li></ul>
<ul class="foot-links" style="left:667px"><li>User Agreement</li><li>Glowvra Street</li><li>Tip Consultant</li></ul>

<div class="foot-title" style="left:825px">Get In Touch</div>
<div class="contact" style="top:3452px">
  <svg width="14" height="14" viewBox="0 0 14 14" fill="#fff"><path d="M3 1l2.5 3-1.3 1.6a8 8 0 004.2 4.2L10 8.5l3 2.5-1.5 2.5C6 13 1 8 .5 2.5z"/></svg>
  <span>Call Us: 555-013-2468</span>
</div>
<div class="contact" style="top:3506px">
  <svg width="14" height="11" viewBox="0 0 14 11" fill="none" stroke="#fff" stroke-width="1.3"><rect x=".7" y=".7" width="12.6" height="9.6"/><path d="M.7 .7L7 6l6.3-5.3"/></svg>
  <span>Email: info@glowvra.com</span>
</div>

<div class="abs foot-rule"></div>
<div class="abs copy">© Copyright 2019 Glowvra.</div>

</body>
</html>
```